Electrical Busness

We require an a5 flyer that promotes our Electrical business. Things we would like included are;
1) our business name, Bright Arc Electrical and Networks
2) Our Electrical license, EC 27351
3) Our ABN, 52 419 086 273
4) Our website, www.tallowwiring.com.au
5) Our Email, info@tallowwiring.com.au
6) Our contact number, 0482 576 104
8) Our logo, I will attach this (can you please change it so the bbackground is white not black)
9) Our colours are red and white and some black
10) 'over 8 years experience'
11) 'call today for a free quote'
12) 'friendly, honest and reliable workmanship'
13) 'local Electrician in your area'
14)' servicing Cannington, Melville, Manning, Thornlie, Victoria Park, Canning Vale, Forrestfeild and many more'
15) 'Renovations, additions, upgrades, new installations, maintenance'
16) 'available 24/7 for emergency call outs'
17) 'LED downlights, smoke alarms, RCDs, smoke detectors, power & USB points, dimmers, data, phone points, switchboard upgrade, security lighting, safety certificate, compliance and safety checks, exit and emergency lighting and many more'
18) 'WA qualified and fully insured'
19) 'QIFA member' (will attach logo)

```html
<!DOCTYPE html>
<html lang="en">
<head>
<meta charset="utf-8">
<title>Bright Arc Electrical and Networks – A5 Flyer</title>
<link href="https://fonts.googleapis.com/css2?family=Oswald:wght@500;600&family=Raleway:wght@500;600;700;800&family=Kalam:wght@400;700&display=swap" rel="stylesheet">
<style>
  :root{
    --red:#d3141b;
    --red-dark:#a50e14;
    --black:#161616;
    --charcoal:#2a2a2a;
    --slate:#3d4957;
    --white:#ffffff;
    --ink:#222222;
    --navy:#1d4f91;
    --backdrop:#ecebe8;
  }
  *{box-sizing:border-box;margin:0;padding:0}
  html,body{width:1200px;height:729px;overflow:hidden}
  body{background:var(--backdrop);position:relative;font-family:'Raleway',sans-serif;color:var(--ink)}
  .icon-defs{position:absolute;width:0;height:0}

  .flyer{position:absolute;top:120px;width:345px;height:488px;background:var(--white);overflow:hidden;box-shadow:0 2px 8px rgba(0,0,0,.18)}
  .flyer--one{left:73px}
  .flyer--two{left:431px}
  .flyer--three{left:794px}

  /* hero photo area */
  .hero-photo{position:absolute;left:0;top:0;width:345px;height:226px}
  .hero-photo--tester{background:linear-gradient(100deg,#e9e4df 0%,#c9c3bf 35%,#3a4c7a 60%,#2b3a63 80%,#d7dbe2 100%)}
  .hero-photo--switchboard{background:linear-gradient(120deg,#2f6fc0 0%,#5d8fd0 25%,#d8dde3 50%,#b9c2cc 75%,#2b4f8a 100%)}
  .hero-photo--worker{background:linear-gradient(90deg,#f3f3f3 0%,#d7dade 30%,#9aa6b8 55%,#2c3444 75%,#f0f0f0 100%)}

  .brand{position:absolute;left:14px;top:14px;width:130px}
  .brand-mark{width:38px;height:38px;border-radius:50%;background:var(--red);margin:0 0 6px 42px}
  .brand-name{font-family:'Raleway',sans-serif;font-weight:800;font-size:10.5px;line-height:1.15;color:var(--red);text-align:center;text-transform:uppercase}

  /* ribbon + badge */
  .ribbon{position:absolute;left:60px;top:141px;width:210px;height:40px;background:var(--red);clip-path:polygon(0 0,100% 0,94% 100%,0 100%)}
  .ribbon-text{position:absolute;left:18px;top:5px;color:var(--white);font-weight:800;font-size:11.5px;line-height:1.15}
  .ribbon-amp{position:absolute;left:146px;top:-1px;font-family:'Kalam',cursive;font-weight:700;font-size:26px;color:var(--white)}
  .ribbon-sub{position:absolute;left:60px;top:181px;width:178px;height:15px;background:var(--charcoal);clip-path:polygon(0 0,100% 0,95% 100%,0 100%)}
  .ribbon-sub span{position:absolute;left:16px;top:-1px;font-family:'Kalam',cursive;font-size:11px;color:var(--red)}

  .badge{position:absolute;left:7px;top:136px;width:66px;height:66px;border-radius:50%;background:var(--white);border:2px dashed #bdbdbd;overflow:hidden}
  .badge-inner{position:absolute;inset:4px;border-radius:50%;overflow:hidden;background:var(--charcoal)}
  .badge-top{height:55%;background:var(--red);color:var(--white);font-family:'Kalam',cursive;font-weight:700;font-size:17px;text-align:center;line-height:32px}
  .badge-bottom{color:var(--white);font-size:5.5px;font-weight:600;text-align:center;line-height:1.2;padding-top:2px}

  /* service area band */
  .area-band{position:absolute;left:0;top:226px;width:345px;height:64px;background:linear-gradient(#1e1e1e,#2c2c2c 60%,#1a1a1a);text-align:center;color:var(--white)}
  .area-title{font-family:'Oswald',sans-serif;font-weight:600;font-size:13px;letter-spacing:.2px;margin-top:5px}
  .area-title em{font-family:'Kalam',cursive;font-style:normal;font-weight:400;font-size:13px}
  .area-list{font-family:'Raleway',sans-serif;font-weight:600;font-size:8px;line-height:1.3;margin-top:1px}
  .area-more{font-family:'Kalam',cursive;font-size:8.5px;line-height:1;margin-left:60px}

  /* service icons */
  .services{position:absolute;left:0;top:292px;width:345px;height:64px;display:flex;background:linear-gradient(var(--red),var(--red-dark))}
  .service{flex:1;border-right:1px solid rgba(255,255,255,.35);text-align:center;color:var(--white)}
  .service:last-child{border-right:none}
  .service svg{width:22px;height:22px;margin-top:12px;fill:none;stroke:var(--white);stroke-width:2}
  .service-label{font-weight:700;font-size:7.3px;margin-top:8px;text-transform:uppercase}

  .extras{position:absolute;left:0;top:357px;width:345px;height:46px;background:var(--black);color:var(--white);font-weight:600;font-size:7.2px;line-height:1.25;text-align:center;padding:5px 10px 0;text-transform:uppercase}

  /* contact */
  .member{position:absolute;left:28px;top:414px;display:flex;align-items:center;gap:8px}
  .member-badge{width:46px;height:14px;background:var(--navy)}
  .member-text{font-size:8px;font-weight:600;color:var(--navy);border-left:1px solid #9db3d3;padding-left:6px}
  .contact{position:absolute;left:202px;top:405px;width:140px}
  .contact-cta{font-family:'Kalam',cursive;font-weight:700;font-size:11px;color:var(--red)}
  .contact-phone{font-weight:700;font-size:11.5px;color:var(--ink);margin-top:1px}
  .contact-web{font-size:7px;font-weight:500;line-height:1.35;color:var(--ink)}

  .licence-bar{position:absolute;left:0;top:455px;width:178px;height:18px;background:var(--slate);clip-path:polygon(0 0,100% 0,88% 100%,0 100%);color:var(--white);font-size:8.5px;font-weight:600;line-height:18px;padding-left:8px}
  .abn-bar{position:absolute;left:160px;top:463px;width:185px;height:18px;background:var(--red);clip-path:polygon(12% 0,100% 0,100% 100%,0 100%);color:var(--white);font-size:8.5px;font-weight:600;line-height:18px;padding-left:48px}
</style>
</head>
<body>

<svg class="icon-defs" aria-hidden="true">
  <symbol id="icon-house" viewBox="0 0 24 24"><path d="M2 12 L10 5 L18 12 M4 11 V21 H16 V11 M8 21 V16 H12 V21"/><path d="M20 20 V6 M17 9 L20 6 L23 9"/></symbol>
  <symbol id="icon-plus" viewBox="0 0 24 24"><circle cx="12" cy="12" r="10"/><path d="M12 7 V17 M7 12 H17" stroke-width="3"/></symbol>
  <symbol id="icon-chart" viewBox="0 0 24 24"><path d="M3 21 V17 M8 21 V14 M13 21 V11 M18 21 V8" stroke-width="3"/><path d="M3 12 L10 7 L14 9 L21 3 M17 3 H21 V7"/></symbol>
  <symbol id="icon-kit" viewBox="0 0 24 24"><rect x="2" y="7" width="20" height="14" rx="2"/><path d="M8 7 V4 H16 V7"/><path d="M7 14 L11 18 L17 11" stroke-width="2.5"/></symbol>
  <symbol id="icon-gears" viewBox="0 0 24 24"><circle cx="9" cy="14" r="4"/><path d="M9 7 V9 M9 19 V21 M2 14 H4 M14 14 H16 M4 9 L5.5 10.5 M12.5 17.5 L14 19 M4 19 L5.5 17.5 M12.5 10.5 L14 9"/><circle cx="18" cy="6" r="2.5"/><path d="M18 1.5 V3 M18 9 V10.5 M13.5 6 H15 M21 6 H22.5"/></symbol>
</svg>

<!-- Flyer variant: tester -->
<article class="flyer flyer--one">
  <div class="hero-photo hero-photo--tester" role="img" aria-label="Electrician in navy overalls testing a circuit with a multimeter, customer blurred in the background"></div>
  <div class="brand"><div class="brand-mark"></div><p class="brand-name">Bright Arc Electrical and Networks</p></div>
  <div class="ribbon"><p class="ribbon-text">friendly, honest<br>reliable workmanship</p><span class="ribbon-amp">&amp;</span></div>
  <div class="ribbon-sub"><span>with over 8 years experience</span></div>
  <div class="badge"><div class="badge-inner"><div class="badge-top">24/7</div><div class="badge-bottom">for emergency<br>call outs</div></div></div>
  <section class="area-band">
    <h2 class="area-title">LOCAL ELECTRICIAN IN YOUR AREA <em>servicing</em></h2>
    <p class="area-list">CANNINGTON, MELVILLE, MANNING, THORNLIE, BELMONT<br>VICTORIA PARK, CANNING VALE, FORRESTFEILD</p>
    <p class="area-more">and many more</p>
  </section>
  <ul class="services">
    <li class="service"><svg><use href="#icon-house"/></svg><p class="service-label">Renovations</p></li>
    <li class="service"><svg><use href="#icon-plus"/></svg><p class="service-label">Additions</p></li>
    <li class="service"><svg><use href="#icon-chart"/></svg><p class="service-label">Upgrades</p></li>
    <li class="service"><svg><use href="#icon-kit"/></svg><p class="service-label">Installations</p></li>
    <li class="service"><svg><use href="#icon-gears"/></svg><p class="service-label">Maintenance</p></li>
  </ul>
  <p class="extras">LED downlights, smoke alarms, RCDs, smoke detectors, power &amp; USB points, dimmers, data, phone points, switchboard upgrade, security lighting, safety certificate, compliance and safety checks, exit and emergency lighting and many more</p>
  <div class="member"><span class="member-badge"></span><span class="member-text">QIFA member</span></div>
  <div class="contact"><p class="contact-cta">Call today for a free quote</p><p class="contact-phone">0482 576 104</p><p class="contact-web">www.tallowwiring.com.au<br>info@tallowwiring.com.au</p></div>
  <div class="licence-bar">ELECTRICAL LICENCE: EC 27351</div>
  <div class="abn-bar">ABN: 52 419 086 273</div>
</article>

<!-- Flyer variant: switchboard -->
<article class="flyer flyer--two">
  <div class="hero-photo hero-photo--switchboard" role="img" aria-label="Electrician in a blue hard hat working on a switchboard with a voltage tester"></div>
  <div class="brand"><div class="brand-mark"></div><p class="brand-name">Bright Arc Electrical and Networks</p></div>
  <div class="ribbon"><p class="ribbon-text">friendly, honest<br>reliable workmanship</p><span class="ribbon-amp">&amp;</span></div>
  <div class="ribbon-sub"><span>with over 8 years experience</span></div>
  <div class="badge"><div class="badge-inner"><div class="badge-top">24/7</div><div class="badge-bottom">for emergency<br>call outs</div></div></div>
  <section class="area-band">
    <h2 class="area-title">LOCAL ELECTRICIAN IN YOUR AREA <em>servicing</em></h2>
    <p class="area-list">CANNINGTON, MELVILLE, MANNING, THORNLIE, BELMONT<br>VICTORIA PARK, CANNING VALE, FORRESTFEILD</p>
    <p class="area-more">and many more</p>
  </section>
  <ul class="services">
    <li class="service"><svg><use href="#icon-house"/></svg><p class="service-label">Renovations</p></li>
    <li class="service"><svg><use href="#icon-plus"/></svg><p class="service-label">Additions</p></li>
    <li class="service"><svg><use href="#icon-chart"/></svg><p class="service-label">Upgrades</p></li>
    <li class="service"><svg><use href="#icon-kit"/></svg><p class="service-label">Installations</p></li>
    <li class="service"><svg><use href="#icon-gears"/></svg><p class="service-label">Maintenance</p></li>
  </ul>
  <p class="extras">LED downlights, smoke alarms, RCDs, smoke detectors, power &amp; USB points, dimmers, data, phone points, switchboard upgrade, security lighting, safety certificate, compliance and safety checks, exit and emergency lighting and many more</p>
  <div class="member"><span class="member-badge"></span><span class="member-text">QIFA member</span></div>
  <div class="contact"><p class="contact-cta">Call today for a free quote</p><p class="contact-phone">0482 576 104</p><p class="contact-web">www.tallowwiring.com.au<br>info@tallowwiring.com.au</p></div>
  <div class="licence-bar">ELECTRICAL LICENCE: EC 27351</div>
  <div class="abn-bar">ABN: 52 419 086 273</div>
</article>

<!-- Flyer variant: worker -->
<article class="flyer flyer--three">
  <div class="hero-photo hero-photo--worker" role="img" aria-label="Electrician in an orange hard hat holding a coiled extension cable, colleagues blurred behind"></div>
  <div class="brand"><div class="brand-mark"></div><p class="brand-name">Bright Arc Electrical and Networks</p></div>
  <div class="ribbon"><p class="ribbon-text">friendly, honest<br>reliable workmanship</p><span class="ribbon-amp">&amp;</span></div>
  <div class="ribbon-sub"><span>with over 8 years experience</span></div>
  <div class="badge"><div class="badge-inner"><div class="badge-top">24/7</div><div class="badge-bottom">for emergency<br>call outs</div></div></div>
  <section class="area-band">
    <h2 class="area-title">LOCAL ELECTRICIAN IN YOUR AREA <em>servicing</em></h2>
    <p class="area-list">CANNINGTON, MELVILLE, MANNING, THORNLIE, BELMONT<br>VICTORIA PARK, CANNING VALE, FORRESTFEILD</p>
    <p class="area-more">and many more</p>
  </section>
  <ul class="services">
    <li class="service"><svg><use href="#icon-house"/></svg><p class="service-label">Renovations</p></li>
    <li class="service"><svg><use href="#icon-plus"/></svg><p class="service-label">Additions</p></li>
    <li class="service"><svg><use href="#icon-chart"/></svg><p class="service-label">Upgrades</p></li>
    <li class="service"><svg><use href="#icon-kit"/></svg><p class="service-label">Installations</p></li>
    <li class="service"><svg><use href="#icon-gears"/></svg><p class="service-label">Maintenance</p></li>
  </ul>
  <p class="extras">LED downlights, smoke alarms, RCDs, smoke detectors, power &amp; USB points, dimmers, data, phone points, switchboard upgrade, security lighting, safety certificate, compliance and safety checks, exit and emergency lighting and many more</p>
  <div class="member"><span class="member-badge"></span><span class="member-text">QIFA member</span></div>
  <div class="contact"><p class="contact-cta">Call today for a free quote</p><p class="contact-phone">0482 576 104</p><p class="contact-web">www.tallowwiring.com.au<br>info@tallowwiring.com.au</p></div>
  <div class="licence-bar">ELECTRICAL LICENCE: EC 27351</div>
  <div class="abn-bar">ABN: 52 419 086 273</div>
</article>

</body>
</html>
```